Redesign of a growing event production company in atlanta!

www.vorquinstage.com - it's Wix.com site and I'd like to keep it within WIX if possible.
We purchased a new logo and we are looking for a redesign.
We specialize in many different aspects of the event production industry and we want our page to be better segmented, with separation between the audio video lighting and wedding services offered.
We also want this cleaned up, showcasing client feedback and highlighted photos. Our industry is very visual and we want some of our work showcased as well as area for event videos.
We want the ability to add new photos and videos as well as links to our blog. If we can incorporate our blog into the site, that would be great as well.
Attached is the new logo, we are going to have it animated and placed on the site as well. We love the color spectrum of light and the significance to event production. We would like the page to incorporate that.
Updates

There are just a few days left, please submit your final versions, with requested revisions.

Target Market(s)

Women are the main purchasees of our services. brides between 20 - 40, and then corporate event planners...we have a high end market. We are marketing to the people who plan galas and society socials.

Industry/Entity Type

It Company

Number of Pages Required

5+ page

Font styles to use
Sans Serif
Script

Requirements
Must have
• incorporate the same content I currently have on my site.
• A clear but fluid separation between our event production services (Audio Visual) and the wedding services we offer. We MUST also be able to clearly show what we do. We are a one stop show and we want to convey that.
Nice to have
• Color palette based off logo attached

```html
<!DOCTYPE html>
<html lang="en">
<head>
<meta charset="utf-8">
<title>Vorquin Stage – Event Production</title>
<link rel="stylesheet" href="https://fonts.googleapis.com/css2?family=Maven+Pro:wght@400;500;700&family=Open+Sans:wght@400;600;700&display=swap">
<style>
:root{
  --pink:#e3179c;
  --lime:#dcdc1f;
  --black:#070708;
  --ink:#2b2b2b;
  --footer:#262626;
  --white:#ffffff;
}
*{box-sizing:border-box;margin:0;padding:0}
html,body{width:1200px;height:3061px;overflow:hidden}
body{position:relative;font-family:"Open Sans",Arial,sans-serif;color:var(--ink);background:var(--white)}
.abs{position:absolute}
.center{text-align:center}

/* Header */
.hero{left:0;top:0;width:1200px;height:660px;background:radial-gradient(ellipse at 50% 45%,#4a5058 0%,#1c1f24 40%,var(--black) 75%)}
.hero-shade{left:0;top:360px;width:1200px;height:300px;background:linear-gradient(180deg,rgba(0,0,0,0) 0%,rgba(0,0,0,.7) 60%,#000 100%)}
.call{left:133px;top:78px;display:flex;align-items:center;gap:12px;color:var(--white)}
.call-icon{width:36px;height:36px;border-radius:50%;background:var(--pink);display:flex;align-items:center;justify-content:center}
.call-label{font-size:15px;color:var(--pink);line-height:1}
.call-number{font-size:21px;font-weight:600;line-height:1.2}
.interact{left:808px;top:60px;color:var(--white);font-size:21px}
.social{left:808px;top:100px;display:flex;gap:10px}
.social span{width:28px;height:28px;border-radius:4px;display:block}
.brand-circle{left:452px;top:30px;width:216px;height:216px;border-radius:50%;background:#1a1a1c;border:6px solid #c9c9c9}
.brand-name{left:0;top:272px;width:1200px;font-family:"Maven Pro",sans-serif;font-size:58px;line-height:1;font-weight:500;color:#d8d8d8;letter-spacing:2px}
.brand-sub{left:0;top:334px;width:1200px;font-family:"Maven Pro",sans-serif;font-size:15px;line-height:1;color:#bcbcbc;letter-spacing:6px}
.intro{left:170px;top:388px;width:860px;color:var(--white);font-size:23px;font-weight:600;line-height:1.6}
.nav{left:133px;top:556px;display:flex;gap:8px}
.nav a{display:flex;align-items:center;justify-content:center;height:52px;background:var(--lime);color:#111;font-size:17px;font-weight:600;text-decoration:none}
.nav a.active{background:var(--pink);color:var(--white);border:3px solid #fff;outline:2px solid var(--pink)}

/* Welcome */
.welcome{left:0;top:660px;width:1200px;height:480px;background:linear-gradient(180deg,#faf9f4,#ebe8dd)}
.welcome-title{left:0;top:688px;width:1200px;font-family:"Maven Pro",sans-serif;font-size:31px;line-height:1.3;font-weight:500;color:var(--pink)}
.welcome-text{left:170px;top:772px;width:860px;font-size:17.5px;line-height:1.5;color:#333}
.welcome-text p+p{margin-top:24px}
.btn{left:526px;top:1044px;width:152px;height:50px;background:var(--pink);color:var(--white);font-weight:700;font-size:17px;display:flex;align-items:center;justify-content:center;border:3px solid #fff;outline:2px solid var(--pink)}

/* Section titles */
.sec-title{left:0;width:1200px;color:var(--white);font-family:"Maven Pro",sans-serif;font-size:31px;line-height:1.3;font-weight:500}
.rule{left:265px;width:670px;height:2px;background:rgba(255,255,255,.6)}
.dots{left:0;width:1200px;color:var(--white);font-size:12px;letter-spacing:4px}

/* Services */
.services{left:0;top:1140px;width:1200px;height:418px;background:var(--pink)}
.card{top:1268px;width:207px;height:248px;background:#222;border:4px solid #fff;box-shadow:0 3px 6px rgba(0,0,0,.3)}
.card-img{width:100%;height:166px}
.card-name{height:74px;display:flex;align-items:center;justify-content:center;text-align:center;color:var(--white);font-size:21px;line-height:1.3}
.arrow{width:50px;height:50px;border-radius:50%;border:2px solid #fff;display:flex;align-items:center;justify-content:center}

/* Showcase */
.showcase{left:0;top:1558px;width:1200px;height:1037px;background:var(--lime)}
.showcase-lead{left:160px;top:1678px;width:880px;color:var(--white);font-size:20px;font-weight:700;line-height:1.65}
.gallery-title{left:0;width:1200px;font-size:19px;font-weight:700;color:#333;text-decoration:underline}
.strip{left:133px;width:935px;height:214px;display:flex}
.strip div{height:100%}
.banner-text{left:260px;top:2400px;width:680px;color:var(--white);font-size:20px;font-weight:700;line-height:1.9}
.banner-left{left:0;top:2390px;width:265px;height:205px;background:linear-gradient(160deg,#3a3a3a,#1c1c1c)}
.banner-right{left:940px;top:2380px;width:260px;height:215px;background:linear-gradient(200deg,#c9a07a,#3b2b24)}

/* Blog & testimonials */
.lower{left:0;top:2595px;width:1200px;height:345px;background:var(--pink)}
.lower-title{font-family:"Maven Pro",sans-serif;font-size:21px;font-weight:500;color:#111}
.lower-rule{height:2px;background:rgba(255,255,255,.8)}
.pager{color:#fff;font-size:18px}
.post{left:133px;width:620px;display:flex;gap:16px}
.post-thumb{width:58px;height:58px;flex:none;border:2px solid #fff}
.post-date{font-size:11px;font-style:italic;color:var(--lime);font-weight:600}
.post-text{font-size:12.5px;color:var(--white);line-height:1.35}
.post-sep{left:133px;width:620px;height:1px;background:rgba(255,255,255,.5)}
.quote{left:790px;top:2672px;width:280px;height:166px;background:var(--white);border-radius:8px;padding:14px 18px 0 36px;font-size:12px;font-style:italic;color:#555;line-height:1.45}
.quote-mark{left:800px;top:2666px;font-size:44px;color:#ccc;font-family:Georgia,serif}
.avatar{left:815px;top:2818px;width:78px;height:78px;border-radius:50%;border:4px solid #fff;background:linear-gradient(160deg,#e9c9a8,#7a5a44)}
.client{left:913px;top:2866px;font-size:13px;font-weight:700;color:var(--white)}

/* Footer */
.footer{left:0;top:2940px;width:1200px;height:121px;background:var(--footer)}
.footer-nav{left:130px;top:2968px;display:flex;font-size:14px;font-weight:600;color:var(--white)}
.footer-nav span{padding:0 8px;border-left:1px solid #999}
.footer-nav span:first-child{border-left:none;padding-left:0}
.copy{left:133px;top:3010px;font-size:13px;color:#bbb}
.footer-mark{left:970px;top:2948px;width:90px;height:90px;border-radius:50%;border:3px solid #555;background:#333}
</style>
</head>
<body>

<header>
  <div class="abs hero" role="img" aria-label="Concert crowd under stage lights"></div>
  <div class="abs hero-shade"></div>

  <div class="abs call">
    <div class="call-icon">
      <svg width="20" height="20" viewBox="0 0 24 24"><path fill="#fff" d="M6.6 10.8a15.1 15.1 0 0 0 6.6 6.6l2.2-2.2c.3-.3.7-.4 1-.2 1.1.4 2.3.6 3.6.6.6 0 1 .4 1 1V20c0 .6-.4 1-1 1A17 17 0 0 1 3 4c0-.6.4-1 1-1h3.5c.6 0 1 .4 1 1 0 1.3.2 2.5.6 3.6.1.3 0 .7-.2 1z"/></svg>
    </div>
    <div>
      <div class="call-label">Call Now</div>
      <div class="call-number">+123 456 7890</div>
    </div>
  </div>

  <div class="abs interact">Interact With Us</div>
  <div class="abs social" aria-label="Social links">
    <span style="background:#d9d9d9"></span>
    <span style="background:#2da3c7"></span>
    <span style="background:#4f7fa8"></span>
    <span style="background:#d6261f"></span>
    <span style="background:#1f75ae"></span>
    <span style="background:#cb2027"></span>
    <span style="background:#3b5a9a"></span>
  </div>

  <div class="abs brand-circle"></div>
  <div class="abs brand-name center">VORQUIN STAGE</div>
  <div class="abs brand-sub center">VORQUIN STAGE PRODUCTION</div>

  <p class="abs intro center">Vorquin Stage is an award winning event production company providing quality, custom event solutions catered to your specific needs from planning and entertainment to audio, video and lighting.</p>

  <nav class="abs nav">
    <a class="active" style="width:148px">Home</a>
    <a style="width:150px">Get Inspired</a>
    <a style="width:150px">Services Offered</a>
    <a style="width:150px">Vorquin Owners</a>
    <a style="width:150px">Client Referrals</a>
    <a style="width:155px">Contact</a>
  </nav>
</header>

<section>
  <div class="abs welcome" role="img" aria-label="Softly lit wedding reception tables"></div>
  <h1 class="abs welcome-title center">WELCOME TO VORQUIN STAGE</h1>
  <div class="abs welcome-text center">
    <p>Vorquin Stage Production's team has diverse professional experience working in professional Entertainment, Catering, Audio/Video Production, Venue Management and Lighting Production. This seperates us from our competition, giving you the best event experience!</p>
    <p>Lorem ipsum dolor sit amet, consectetur adipiscing elit. Proin tellus est, convallis quis sodales nec, interdum ac massa. Praesent molestie dolor in nisl pellentesque, eu suscipit orci semper. Mauris condimentum elementum imperdiet. Fusce interdum hendrerit erat, non lacinia mauris. Cras in convallis odio, non semper felis. Quisque pellentesque, odio sagittis dapibus ultricies, mi est vestibulum neque, vel tempor enim quam sit amet diam. Mauris quis sem sapien.</p>
  </div>
  <div class="abs btn">Read More</div>
</section>

<section>
  <div class="abs services"></div>
  <h2 class="abs sec-title center" style="top:1170px">OUR SERVICES</h2>
  <div class="abs rule" style="top:1222px"></div>
  <div class="abs dots center" style="top:1220px">●●●</div>

  <div class="abs arrow" style="left:61px;top:1343px"><svg width="16" height="16" viewBox="0 0 16 16"><path d="M10 2 4 8l6 6" stroke="#fff" stroke-width="2" fill="none"/></svg></div>
  <div class="abs arrow" style="left:1087px;top:1343px"><svg width="16" height="16" viewBox="0 0 16 16"><path d="m6 2 6 6-6 6" stroke="#fff" stroke-width="2" fill="none"/></svg></div>

  <div class="abs card" style="left:140px"><div class="card-img" role="img" aria-label="Audio mixing console" style="background:linear-gradient(160deg,#c9394a,#2a2a33)"></div><div class="card-name">Audio Visual<br>Production</div></div>
  <div class="abs card" style="left:383px"><div class="card-img" role="img" aria-label="DJ performing to a crowd" style="background:linear-gradient(180deg,#e8e8e8,#3a3a3a)"></div><div class="card-name">Disc Jockeys and<br>Emcees</div></div>
  <div class="abs card" style="left:622px"><div class="card-img" role="img" aria-label="Blue event lighting on a ceiling" style="background:radial-gradient(circle,#58b4ff,#0b1e8a)"></div><div class="card-name">Event<br>Lighting</div></div>
  <div class="abs card" style="left:852px"><div class="card-img" role="img" aria-label="Elegant banquet table setting" style="background:linear-gradient(160deg,#f2efe6,#b9ad94)"></div><div class="card-name">Event<br>Planning</div></div>
</section>

<section>
  <div class="abs showcase"></div>
  <h2 class="abs sec-title center" style="top:1588px">OUR SHOWCASE</h2>
  <div class="abs rule" style="top:1640px"></div>
  <div class="abs dots center" style="top:1638px">●●●</div>
  <p class="abs showcase-lead center">Lorem ipsum dolor sit amet consectetur adipiscing elit proin tellus est convallis quis sodales nec interdum ac massa.</p>

  <div class="abs gallery-title center" style="top:1788px">Event Gallery</div>
  <div class="abs strip" style="top:1834px" role="img" aria-label="Event photo gallery">
    <div style="width:75px;background:linear-gradient(#3a5cc8,#162060)"></div>
    <div style="width:228px;background:linear-gradient(#c8743a,#3a1a10)"></div>
    <div style="width:232px;background:linear-gradient(#6a4ab0,#1a1030)"></div>
    <div style="width:232px;background:linear-gradient(#d44ad0,#3a1048)"></div>
    <div style="width:168px;background:linear-gradient(#e33a3a,#4a0c0c)"></div>
  </div>
  <div class="abs arrow" style="left:61px;top:1916px"><svg width="16" height="16" viewBox="0 0 16 16"><path d="M10 2 4 8l6 6" stroke="#fff" stroke-width="2" fill="none"/></svg></div>
  <div class="abs arrow" style="left:1087px;top:1916px"><svg width="16" height="16" viewBox="0 0 16 16"><path d="m6 2 6 6-6 6" stroke="#fff" stroke-width="2" fill="none"/></svg></div>

  <div class="abs gallery-title center" style="top:2098px">Wedding Gallery</div>
  <div class="abs strip" style="top:2142px" role="img" aria-label="Wedding photo gallery">
    <div style="width:305px;background:linear-gradient(#d8d2c8,#6a5f55)"></div>
    <div style="width:232px;background:linear-gradient(#9a9a9a,#2a2a2a)"></div>
    <div style="width:232px;background:linear-gradient(#f2f2f2,#a8b4a0)"></div>
    <div style="width:166px;background:linear-gradient(#cfe0f0,#6a8a5a)"></div>
  </div>
  <div class="abs arrow" style="left:61px;top:2225px"><svg width="16" height="16" viewBox="0 0 16 16"><path d="M10 2 4 8l6 6" stroke="#fff" stroke-width="2" fill="none"/></svg></div>
  <div class="abs arrow" style="left:1087px;top:2225px"><svg width="16" height="16" viewBox="0 0 16 16"><path d="m6 2 6 6-6 6" stroke="#fff" stroke-width="2" fill="none"/></svg></div>

  <div class="abs banner-left" role="img" aria-label="Camera operator filming an event"></div>
  <div class="abs banner-right" role="img" aria-label="Bride and groom portrait"></div>
  <p class="abs banner-text center">Lorem ipsum dolor sit amet, consectetur adipiscing elit. Phasellus tempor aliquam nunc, vel euismod est dignissim vitae. Sed tristique egestas libero ut lobortis. Nam dapibus imperdiet ligula sit amet facilisis. Duis vitae nunc diam.</p>
</section>

<section>
  <div class="abs lower"></div>
  <h3 class="abs lower-title" style="left:133px;top:2618px">LATEST BLOG POSTS</h3>
  <div class="abs lower-rule" style="left:133px;top:2652px;width:620px"></div>
  <div class="abs pager" style="left:722px;top:2620px">‹ ›</div>

  <div class="abs post" style="top:2672px"><div class="post-thumb" role="img" aria-label="Author photo" style="background:#3a3a3a"></div><div><div class="post-date">January 1, 2014 - 3:00-4:00pm</div><div class="post-text">Lorem ipsum dolor sit amet, consectetur adipiscing elit. Pellente in efficitur lectus. Nun laoreet quis odio sed lob vulputate erat quis leo placerat tincidunt</div></div></div>
  <div class="abs post-sep" style="top:2744px"></div>
  <div class="abs post" style="top:2764px"><div class="post-thumb" role="img" aria-label="Author photo" style="background:#c98a5a"></div><div><div class="post-date">January 1, 2014 - 3:00-4:00pm</div><div class="post-text">Lorem ipsum dolor sit amet, consectetur adipiscing elit. Pellente in efficitur lectus. Nun laoreet quis odio sed lob vulputate erat quis leo placerat tincidunt</div></div></div>
  <div class="abs post-sep" style="top:2836px"></div>
  <div class="abs post" style="top:2852px"><div class="post-thumb" role="img" aria-label="Author photo" style="background:#6a7a8a"></div><div><div class="post-date">January 1, 2014 - 3:00-4:00pm</div><div class="post-text">Lorem ipsum dolor sit amet, consectetur adipiscing elit. Pellente in efficitur lectus. Nun laoreet quis odio sed lob vulputate erat quis leo placerat tincidunt</div></div></div>

  <h3 class="abs lower-title" style="left:790px;top:2622px">CLIENT TESTIMONIALS</h3>
  <div class="abs lower-rule" style="left:790px;top:2656px;width:280px"></div>
  <div class="abs pager" style="left:1036px;top:2620px">‹ ›</div>
  <div class="abs quote">Lorem ipsum dolor sit amet consectetur sed diam nibh tincidunt ut laoreet dolore magna erat volutpat wisi enim ad minim veniam quis nostrud exerci tation ipsum dolor sit amet sed diam nonummy nibh euismod tincidunt ut laoreet dolore magna aliquam volutpat.</div>
  <div class="abs quote-mark">“</div>
  <div class="abs avatar" role="img" aria-label="Client portrait"></div>
  <div class="abs client">Mr. Elias Brandt</div>
</section>

<footer>
  <div class="abs footer"></div>
  <div class="abs footer-nav"><span>Home</span><span>Get Inspired</span><span>Services Offered</span><span>Vorquin Owners</span><span>Client Referrals</span><span>Contact</span></div>
  <div class="abs copy">© 2015 Vorquin Stage, LLC. All Rights Reserved.</div>
  <div class="abs footer-mark"></div>
</footer>

</body>
</html>
```